Mortgage Specialist Wordpress Build

I have a current WordPress site but I would like a whole new site built using the same domain. I've included a site for reference in my outline. The main focus of the website is to educate and capture leads.
I would like my blogs to stay for SEO already earned. Please see work requested attached.
Updates
Project Deadline Extended Reason: I am extending the deadline because I didn't realize this was a design only and I need the website coded as well. I've purchased the add-on. This is my first time using Pixel Guild so please bare with me. I have additional Wordpress sites I want to have built too. Thanks, Colin Added Tuesday, April 18, 2017
Target Market(s)
Home Buyers, Home owners looking to refinance or renew their mortgages
Industry/Entity Type
Mortgage
Coding
Coded - Design and coding required
Font styles to use
Look and feel
Each slider illustrates characteristics of the customer's brand and the style your logo design should communicate.

```html
<!DOCTYPE html>
<html lang="en">
<head>
<meta charset="utf-8">
<title>Harbourline Lending Centres – Mortgage Specialist</title>
<link rel="stylesheet" href="https://fonts.googleapis.com/css2?family=Poppins:wght@400;500;600&family=Open+Sans:wght@400;600&family=Oswald:wght@400;500&display=swap">
<style>
  :root{
    --navy:#0d3a78;
    --navy-dark:#0a2d5e;
    --gold:#e8c81e;
    --gold-deep:#d8b513;
    --ink:#2b2b2b;
    --body:#555;
    --card-border:#e4e4e4;
    --card-bg:#fafafa;
    --footer:#1e1e1e;
    --footer-bar:#181818;
    --footer-text:#d6d6d6;
    --partner-mark:#9a9a9a;
    --white:#fff;
  }
  *{box-sizing:border-box;margin:0;padding:0}
  html,body{width:1200px;height:2539px;overflow:hidden}
  body{position:relative;background:var(--white);font-family:"Open Sans",sans-serif;color:var(--body)}
  .abs{position:absolute}

  /* Hero */
  .hero{position:absolute;left:0;top:0;width:1200px;height:668px;overflow:hidden}
  .hero-photo{position:absolute;inset:0;background:
    linear-gradient(180deg,rgba(20,28,40,.55) 0%,rgba(20,28,40,.35) 40%,rgba(20,28,40,.45) 100%),
    linear-gradient(160deg,#5d6b78 0%,#4a5560 30%,#3d4a3a 60%,#4f5a3a 80%,#6a4a4a 100%)}
  .hero-wave{position:absolute;left:0;top:560px}
  .brand{position:absolute;left:100px;top:62px;display:flex;align-items:center;gap:14px}
  .brand-mark{width:30px;height:30px;background:var(--gold)}
  .brand-name{font-family:"Poppins",sans-serif;font-weight:600;font-size:21px;color:var(--white);line-height:1.15;letter-spacing:.5px}
  .nav{position:absolute;top:62px;right:100px;display:flex;gap:30px}
  .nav a{font-family:"Poppins",sans-serif;font-weight:500;font-size:14px;color:var(--white);text-decoration:none}
  .play{position:absolute;left:572px;top:230px}
  .hero-title{position:absolute;left:0;width:1200px;top:298px;text-align:center;font-family:"Poppins",sans-serif;font-weight:600;font-size:56px;color:var(--white);letter-spacing:1px}
  .hero-btn{position:absolute;top:394px;height:37px;border-radius:19px;font-family:"Poppins",sans-serif;font-size:16px;color:var(--white);display:flex;align-items:center;justify-content:center}
  .btn-primary{left:437px;width:155px;background:var(--navy)}
  .btn-ghost{left:608px;width:156px;border:1.5px solid var(--white)}
  .dots{position:absolute;top:466px;left:566px;display:flex;gap:9px;align-items:center}
  .dot{width:10px;height:10px;border-radius:50%;background:#fff}
  .dot.active{width:16px;height:16px;border:2px solid #fff;background:transparent;position:relative}
  .dot.active::after{content:"";position:absolute;left:3px;top:3px;width:6px;height:6px;border-radius:50%;background:#fff}

  /* Help */
  .help-title{left:96px;top:752px;font-family:"Poppins",sans-serif;font-weight:500;font-size:26px;color:var(--ink)}
  .help-text{left:96px;top:800px;width:305px;font-size:11.5px;line-height:19px;color:#666}
  .help-text p{margin-bottom:10px}
  .arrows{left:96px;top:976px;display:flex;gap:6px}
  .arrow{width:28px;height:28px;border-radius:50%;background:#222;display:flex;align-items:center;justify-content:center}
  .card{position:absolute;top:745px;width:211px;height:290px;border:1px solid var(--card-border);background:var(--card-bg);text-align:center}
  .card-icon{position:absolute;left:59px;top:26px;width:92px;height:92px;border-radius:50%;background:var(--navy);box-shadow:inset 0 0 0 3px var(--navy),inset 0 0 0 5px #fff;display:flex;align-items:center;justify-content:center}
  .card h3{position:absolute;top:132px;width:100%;font-family:"Poppins",sans-serif;font-weight:500;font-size:17px;color:var(--navy)}
  .card p{position:absolute;top:162px;left:24px;right:24px;font-size:11px;line-height:21px;color:#555}
  .card-btn{position:absolute;left:57px;top:238px;width:96px;height:27px;background:var(--navy);color:#fff;font-family:"Poppins",sans-serif;font-size:11px;display:flex;align-items:center;justify-content:center}

  /* Questions band */
  .questions{position:absolute;left:0;top:1114px;width:1200px;height:452px;background:
    linear-gradient(90deg,rgba(0,0,0,.45),rgba(0,0,0,.35)),
    linear-gradient(100deg,#3a3a3a 0%,#6a6a6a 25%,#4a4a4a 45%,#2a2a2a 60%,#5a5a4a 80%,#3a3a30 100%)}
  .questions h2{position:absolute;top:200px;width:100%;text-align:center;font-family:"Oswald",sans-serif;font-weight:400;font-size:36px;color:#fff}
  .q-btn{position:absolute;left:514px;top:265px;width:172px;height:36px;border-radius:18px;background:var(--gold);color:#fff;font-family:"Poppins",sans-serif;font-weight:500;font-size:17px;display:flex;align-items:center;justify-content:center}

  /* Broker */
  .broker{position:absolute;left:0;top:1566px;width:1200px;height:399px;background:linear-gradient(180deg,#ecd028,var(--gold) 60%,#e2c31a)}
  .portrait{position:absolute;left:115px;top:75px;width:248px;height:248px;border-radius:50%;border:4px solid #fff;background:radial-gradient(circle at 50% 45%,#8a8e94,#4f5358 70%,#2e3136)}
  .broker h2{position:absolute;left:435px;top:72px;font-family:"Oswald",sans-serif;font-weight:500;font-size:34px;line-height:44px;color:#2a2a2a}
  .broker-text{position:absolute;left:435px;top:136px;width:680px;font-size:11px;line-height:21px;color:#3a3a3a;letter-spacing:-.1px}
  .broker-text p{margin-bottom:10px}
  .read-more{position:absolute;left:435px;top:309px;width:97px;height:28px;background:#2a2a2a;border:1px solid #fff;color:#fff;font-size:13px;display:flex;align-items:center;justify-content:center}

  /* Partners */
  .partners{position:absolute;left:0;top:1965px;width:1200px;height:203px;display:flex;align-items:center;justify-content:center;gap:44px}
  .partner{display:flex;align-items:center;gap:8px;font-family:"Poppins",sans-serif;font-weight:600;font-size:17px;color:#333}
  .partner i{display:block;width:20px;height:20px;background:var(--partner-mark)}

  /* Footer */
  .footer{position:absolute;left:0;top:2168px;width:1200px;height:306px;background:var(--footer);color:var(--footer-text)}
  .footer h4{position:absolute;top:62px;font-family:"Oswald",sans-serif;font-weight:400;font-size:18px;color:#fff}
  .contact-addr{position:absolute;left:96px;top:112px;font-size:11.5px;line-height:19px}
  .contact-line{position:absolute;left:100px;display:flex;align-items:center;gap:14px;font-size:11.5px}
  .socials{position:absolute;left:100px;top:241px;display:flex;gap:5px}
  .socials span{width:20px;height:20px;border-radius:50%;border:1px solid #bbb}
  .news-text{position:absolute;left:394px;top:107px;width:240px;font-size:11px;line-height:19px}
  .news-input{position:absolute;left:394px;top:159px;width:246px;height:42px;background:#fff;color:#666;font-size:11px;padding-left:14px;display:flex;align-items:center}
  .news-btn{position:absolute;left:394px;top:218px;width:123px;height:33px;background:var(--gold-deep);color:#fff;font-size:12px;display:flex;align-items:center;justify-content:center}
  .links{position:absolute;left:741px;top:108px;list-style:none}
  .links li{display:flex;align-items:center;gap:12px;font-size:11px;height:22px}
  .badge-box{position:absolute;left:921px;top:69px;width:180px;height:150px;background:#fff;display:flex;align-items:center;justify-content:center}
  .badge{width:100px;height:100px;border-radius:50%;background:var(--navy-dark);box-shadow:0 0 0 4px #fff,0 0 0 6px var(--navy-dark)}
  .footer-bar{position:absolute;left:0;top:2474px;width:1200px;height:65px;background:var(--footer-bar);border-top:1px solid #333;color:#ccc;font-size:11px;display:flex;align-items:center;justify-content:center}
</style>
</head>
<body>

<header class="hero">
  <div class="hero-photo" role="img" aria-label="Photo of a two-storey family home with a garden and a for-sale sign under an overcast sky"></div>
  <svg class="hero-wave" width="1200" height="108" viewBox="0 0 1200 108">
    <path d="M0 36 L600 105 L1200 36 L1200 108 L0 108 Z" fill="#fff"/>
    <path d="M0 36 L600 105 L1200 36" fill="none" stroke="#e8c81e" stroke-width="5"/>
  </svg>
  <div class="brand"><span class="brand-mark"></span><span class="brand-name">Harbourline<br>Lending Centres</span></div>
  <nav class="nav"><a href="#">HOME</a><a href="#">ABOUT</a><a href="#">BLOG</a><a href="#">CONTACT US</a></nav>
  <svg class="play" width="56" height="56" viewBox="0 0 56 56"><circle cx="28" cy="28" r="26" fill="none" stroke="#fff" stroke-width="2.5"/><path d="M22 17 L38 28 L22 39 Z" fill="none" stroke="#fff" stroke-width="2.5" stroke-linejoin="round"/></svg>
  <h1 class="hero-title">Mortgage Specialist</h1>
  <a class="hero-btn btn-primary">Get Hooked Up</a>
  <a class="hero-btn btn-ghost">I'm a Client</a>
  <div class="dots"><span class="dot active"></span><span class="dot"></span><span class="dot"></span><span class="dot"></span></div>
</header>

<section>
  <h2 class="abs help-title">I NEED HELP WITH</h2>
  <div class="abs help-text">
    <p>Sed ut perspiciatis unde omnis iste natus error sit voluptatem accusantium doloremque laudantium, totam rem aperiam, eaque ipsa quae ab illo inventore veritatis et quasi architecto beatae vitae dicta sunt explicabo. Nemo enim ipsam voluptatem</p>
    <p>Sed ut perspiciatis unde omnis iste natus error sit voluptatem accusantium doloremque laudantium, totam</p>
  </div>
  <div class="abs arrows">
    <span class="arrow"><svg width="10" height="10" viewBox="0 0 10 10"><path d="M6.5 1.5 L3 5 L6.5 8.5" fill="none" stroke="#fff" stroke-width="1.8"/></svg></span>
    <span class="arrow"><svg width="10" height="10" viewBox="0 0 10 10"><path d="M3.5 1.5 L7 5 L3.5 8.5" fill="none" stroke="#fff" stroke-width="1.8"/></svg></span>
  </div>

  <article class="card" style="left:428px">
    <div class="card-icon"><svg width="40" height="40" viewBox="0 0 40 40"><path d="M6 6 H19 L35 22 L22 35 L6 19 Z" fill="#fff"/><circle cx="13" cy="13" r="3" fill="#0d3a78"/></svg></div>
    <h3>Purchase</h3>
    <p>Purchasing a home can be a daunting task as the market continues to sizzle and</p>
    <a class="card-btn">APPLY NOW</a>
  </article>
  <article class="card" style="left:660px">
    <div class="card-icon"><svg width="40" height="40" viewBox="0 0 40 40"><path d="M31 15 A12 12 0 0 0 9 15" fill="none" stroke="#fff" stroke-width="4"/><path d="M34 8 V17 H25 Z" fill="#fff"/><path d="M9 25 A12 12 0 0 0 31 25" fill="none" stroke="#fff" stroke-width="4"/><path d="M6 32 V23 H15 Z" fill="#fff"/></svg></div>
    <h3>Refinance</h3>
    <p>Purchasing a home can be a daunting task as the market continues to sizzle and</p>
    <a class="card-btn">APPLY NOW</a>
  </article>
  <article class="card" style="left:887px">
    <div class="card-icon"><svg width="40" height="40" viewBox="0 0 40 40"><path d="M13 18 V12 A7 7 0 0 1 27 11" fill="none" stroke="#fff" stroke-width="4"/><rect x="9" y="18" width="22" height="17" rx="2" fill="#fff"/><rect x="18.5" y="23" width="3" height="7" fill="#0d3a78"/></svg></div>
    <h3>Renew</h3>
    <p>It's best to start looking for new financing 120 days before your maturity. It's never a good</p>
    <a class="card-btn">APPLY NOW</a>
  </article>
</section>

<section class="questions" role="img" aria-label="Photo of people working together at a desk with a laptop">
  <h2>MORTGAGE OR REAL ESTATE QUESTIONS?</h2>
  <a class="q-btn">Ask Questions</a>
</section>

<section class="broker">
  <div class="portrait" role="img" aria-label="Portrait photo of the mortgage broker"></div>
  <h2>NORTH VANCOUVER MORTGAGE BROKER</h2>
  <div class="broker-text">
    <p>Purchasing a home, refinancing a mortgage and renewing a mortgage have one thing in common: they can represent an exciting time in an individual's life but they can also be complex. I am dedicated to giving back to the region by helping people save thousands of dollars in interest and prepayment expenses and find solutions that are fitted to your specific situation.</p>
    <p>In addition to getting you a fantastic rate, I ensure that I take enough time for each and every one of my clients to go over every detail in order to see that their mortgage repayment schedule is on track with their financial objectives. It is my mission to help people in this wonderful area get the best North Vancouver mortgage package possible while providing tremendous care and service.</p>
  </div>
  <a class="read-more">Read More</a>
</section>

<section class="partners">
  <span class="partner"><i></i>Kestrel Bank</span>
  <span class="partner"><i></i>Alderly Trust</span>
  <span class="partner"><i></i>Quorvane</span>
  <span class="partner"><i></i>Fennick Financial</span>
  <span class="partner"><i></i>Brightmoor</span>
  <span class="partner"><i></i>Solwen Savings</span>
</section>

<footer class="footer">
  <h4 style="left:96px">CONTACT US</h4>
  <div class="contact-addr">Harbourline lending centres 9, Level 2<br>14-18 Bay Street Millbrook NSW 2299</div>
  <div class="contact-line" style="top:177px"><svg width="16" height="16" viewBox="0 0 16 16"><path d="M3 1.5 L6 1.5 L7 5 L5 6.5 C6 8.5 7.5 10 9.5 11 L11 9 L14.5 10 L14.5 13 C14.5 14 13.5 14.5 12.5 14.5 C6.5 14 2 9.5 1.5 3.5 C1.5 2.5 2 1.5 3 1.5 Z" fill="none" stroke="#ddd" stroke-width="1.2"/></svg>Phone: 0400 555 019</div>
  <div class="contact-line" style="top:205px"><svg width="16" height="12" viewBox="0 0 16 12"><rect x=".6" y=".6" width="14.8" height="10.8" fill="none" stroke="#ddd" stroke-width="1.2"/><path d="M.6 .6 L8 7 L15.4 .6" fill="none" stroke="#ddd" stroke-width="1.2"/></svg>Email: info@colinmarsh.com</div>
  <div class="socials"><span></span><span></span><span></span><span></span><span></span></div>

  <h4 style="left:394px">SIGN UP FOR NEWSLETTER</h4>
  <p class="news-text">Excepteur sint occaecat cupidatat non proident, sunt in culpa qui officia deserunt</p>
  <div class="news-input">Enter email</div>
  <a class="news-btn">SUBSCRIPTION</a>

  <h4 style="left:741px">QUICK LINKS</h4>
  <ul class="links">
    <li><svg width="12" height="12" viewBox="0 0 12 12"><circle cx="6" cy="6" r="6" fill="#ddd"/><path d="M5 3.5 L7.5 6 L5 8.5" fill="none" stroke="#1e1e1e" stroke-width="1.5"/></svg>Home</li>
    <li><svg width="12" height="12" viewBox="0 0 12 12"><circle cx="6" cy="6" r="6" fill="#ddd"/><path d="M5 3.5 L7.5 6 L5 8.5" fill="none" stroke="#1e1e1e" stroke-width="1.5"/></svg>About Us</li>
    <li><svg width="12" height="12" viewBox="0 0 12 12"><circle cx="6" cy="6" r="6" fill="#ddd"/><path d="M5 3.5 L7.5 6 L5 8.5" fill="none" stroke="#1e1e1e" stroke-width="1.5"/></svg>Services</li>
    <li><svg width="12" height="12" viewBox="0 0 12 12"><circle cx="6" cy="6" r="6" fill="#ddd"/><path d="M5 3.5 L7.5 6 L5 8.5" fill="none" stroke="#1e1e1e" stroke-width="1.5"/></svg>Blog</li>
    <li><svg width="12" height="12" viewBox="0 0 12 12"><circle cx="6" cy="6" r="6" fill="#ddd"/><path d="M5 3.5 L7.5 6 L5 8.5" fill="none" stroke="#1e1e1e" stroke-width="1.5"/></svg>Contact Us</li>
  </ul>

  <div class="badge-box"><span class="badge"></span></div>
</footer>
<div class="footer-bar">©2017 Harbourline lending centres, All Rights Reserved.</div>

</body>
</html>
```